STICKER DESIGN required for packaging. UK START UP TEA BUSINESS

We are looking for a design for a sticker that will be applied to packaging for our teas! We are a new start up Tea business based in the UK called 'BrookMints'
Selling quality loose leaf tea and teabags via our online shop and also face to face at farmers markets / food shows and eventually in our own tea emporium. We will be marketing our teas to hotels, cafes, delis etc. too
We carry every day teas eg. breakfast blends and also speciality and rare teas to offer customers the chance to try something new. Tea as a treat / ritual / indulgence / healthy lifestyle choice / modern
The design will initially be printed on vinyl stickers and then applied to the tea packaging (pouch bags in matte black and matte silver), in the future the design may be printed direct onto our packaging. The sticker design will need to be scalable as the size of the pouch bag varies dependant on the tea.
The sticker we have in mind is a leaf shape (sketch attached)
colour green to match our logo
It will include our logo (files attached)
Text to be included on the sticker is
- www.brookmints.co.uk
- Dellow, England
- The tea type eg. Green
It will need to complement both black and silver pouches that we are using to package our teas (see attached image of our pouches)
Colours - green leaf, see our corporate colours (green & orange) on our logo files attached. We also like silver and black.
Font - nothing to swirly, must be easy to read on the packaging
once a sticker design is agreed for the initial tea type (Green) we will require additional files for each tea type that we stock. Just the tea type (Green) to be updated - the rest of the design to stay the same. The tea types we stock are listed below
Green
Black
Oolong
White
Herbal
Blended
Happy to answer any questions and aim to give feedback daily! Thank you for your interest
Best regards

```html
<!DOCTYPE html>
<html lang="en">
<head>
<meta charset="utf-8">
<title>BrookMints Green Tea Sticker</title>
<link rel="stylesheet" href="https://fonts.googleapis.com/css2?family=Comfortaa:wght@400;500&display=swap">
<style>
  :root {
    --backdrop: #d3cfc9;
    --leaf-green: #8cc63f;
    --label-white: #ffffff;
  }
  html, body {
    margin: 0;
    padding: 0;
    width: 1157px;
    height: 1200px;
    overflow: hidden;
    background: var(--backdrop);
  }
  .canvas {
    position: relative;
    width: 1157px;
    height: 1200px;
  }
  .sticker {
    position: absolute;
    left: 88px;
    top: 200px;
    width: 980px;
    height: 800px;
  }
  .leaf-shape { fill: var(--leaf-green); }
  .sticker-text {
    font-family: "Comfortaa", sans-serif;
    fill: var(--label-white);
  }
  .brand-name { font-size: 14px; font-weight: 500; }
  .tea-type { font-size: 58px; font-weight: 400; letter-spacing: -1px; }
  .tea-word { font-size: 30px; font-weight: 400; }
  .web-address { font-size: 14.5px; font-weight: 400; }
  .location { font-size: 14.5px; font-weight: 400; }
  .brand-dot { fill: var(--label-white); }
</style>
</head>
<body>
<main class="canvas">
  <svg class="sticker" viewBox="0 0 380 310" xmlns="http://www.w3.org/2000/svg" aria-label="BrookMints Green Tea leaf sticker">
    <path class="leaf-shape" d="M370,5 C330,20 330,35 318,50 C335,44 345,42 354,42 C330,80 320,150 275,177 C240,205 170,225 90,250 C60,262 35,285 12,306 L4,300 C20,280 30,262 38,240 C25,180 45,100 120,50 C190,10 290,5 370,5 Z"/>

    <circle class="brand-dot" cx="188" cy="38" r="7"/>
    <text class="sticker-text brand-name" x="188" y="70" text-anchor="middle">BrookMints</text>

    <text class="sticker-text tea-type" x="183" y="130" text-anchor="middle">Green</text>
    <text class="sticker-text tea-word" x="184" y="168" text-anchor="middle">Tea</text>

    <text class="sticker-text web-address" x="152" y="207" text-anchor="middle" transform="rotate(-12 152 207)">www.brookmints.co.uk</text>
    <text class="sticker-text location" x="290" y="122" text-anchor="middle" transform="rotate(-55 290 122)">Dellow, England</text>
  </svg>
</main>
</body>
</html>
```